Letterhead design for business

Looking for an attractive and professional letterhead that uses the logo that is attached below.

Target Market(s)

Potential bankruptcy clients.

Industry/Entity Type

Legal

Colors

Designer to choose colors to be used in the design.

Requirements
Must have
• Address for locations, phone number, and website address.
• Addresses are on website larkmoorfirm.legal. Use following phone number (for tracking purposes): 404-731-2864

```html
<!DOCTYPE html>
<html lang="en">
<head>
<meta charset="utf-8">
<title>Larkmoor Law Group Letterhead</title>
<link href="https://fonts.googleapis.com/css2?family=Open+Sans:wght@400;500;600&family=Arimo:wght@400&display=swap" rel="stylesheet">
<style>
  :root {
    --charcoal: #414142;
    --green: #7dbf86;
    --ink: #4a4a4a;
    --paper: #ffffff;
    --footer-text: #ffffff;
  }
  * { margin: 0; padding: 0; box-sizing: border-box; }
  html, body { width: 1040px; height: 1200px; overflow: hidden; background: var(--paper); }
  .letterhead {
    position: relative;
    width: 1040px;
    height: 1200px;
    background: var(--paper);
    font-family: "Open Sans", sans-serif;
    color: var(--ink);
  }
  .page-bands { position: absolute; inset: 0; }
  .brand {
    position: absolute;
    top: 92px;
    right: 105px;
    display: flex;
    align-items: center;
    gap: 16px;
  }
  .brand-dot { width: 40px; height: 40px; border-radius: 50%; background: var(--green); }
  .brand-rule { width: 2px; height: 72px; background: var(--green); }
  .brand-name { font-size: 30px; font-weight: 500; color: var(--charcoal); letter-spacing: -0.3px; }
  .letter-body {
    position: absolute;
    left: 97px;
    top: 218px;
    width: 843px;
    font-size: 15.5px;
    line-height: 18px;
  }
  .issue-date { margin-bottom: 19px; }
  .recipient { margin-bottom: 48px; }
  .salutation { margin-bottom: 28px; }
  .body-copy p {
    line-height: 27.2px;
    text-align: justify;
    hyphens: auto;
    margin-bottom: 27px;
  }
  .closing {
    position: absolute;
    left: 97px;
    top: 814px;
    font-size: 15.5px;
    line-height: 18px;
  }
  .signature-mark {
    display: block;
    width: 212px;
    height: 20px;
    margin: 16px 0 16px;
    background: linear-gradient(90deg, #d9d9d9, #ececec);
    border-radius: 10px;
  }
  .signer-name { font-size: 19px; font-weight: 500; color: #3d3d3d; line-height: 24px; }
  .signer-title { font-size: 15.5px; margin-top: 6px; }
  .footer-contact {
    position: absolute;
    right: 70px;
    bottom: 35px;
    text-align: right;
    font-family: "Arimo", sans-serif;
    color: var(--footer-text);
    font-size: 18.5px;
  }
  .footer-line-top { margin-bottom: 14px; }
  .accent { color: var(--green); }
  .sep { margin: 0 9px; }
  .sep-green { color: var(--green); margin: 0 9px; }
</style>
</head>
<body>
<main class="letterhead">
  <svg class="page-bands" width="1040" height="1200" viewBox="0 0 1040 1200" aria-hidden="true">
    <path fill="var(--charcoal)" d="M0 0 H1040 V34 Q520 52 0 34 Z"/>
    <path fill="none" stroke="var(--green)" stroke-width="5" d="M0 48 Q520 66 1040 48"/>
    <path fill="none" stroke="var(--green)" stroke-width="5" d="M0 1078 Q520 1060 1040 1078"/>
    <path fill="var(--charcoal)" d="M0 1092 Q520 1074 1040 1092 V1200 H0 Z"/>
  </svg>

  <header class="brand">
    <span class="brand-dot"></span>
    <span class="brand-rule"></span>
    <span class="brand-name">Larkmoor Law Group</span>
  </header>

  <section class="letter-body">
    <p class="issue-date">Issuing Date: May 5, 2018</p>
    <p class="recipient">Name Of Employee Mr. XYZABC<br>Address of Employee<br>Address Line 2 etc..</p>
    <p class="salutation">Dear Mr.XYZABC</p>
    <div class="body-copy">
      <p>Lorem Ipsum has been the industry's standard dummy text ever since the 1500s, when an unknown printer took a galley of type and scrambled it to make a type specimen book. It has survived not only five centuries, but also the leap into electronic typesetting, remaining essentially unchanged. It was popularised in the 1960s with the release of printed sheets containing Lorem Ipsum passages, and more recently with desktop layout software including versions of Lorem Ipsum.</p>
      <p>Lorem Ipsum is simply dummy text of the printing and typesetting industry. Lorem Ipsum has been the industry's standard dummy text ever since the 1500s, when an unknown printer took a galley of type and scrambled it to make a type specimen book.</p>
      <p>It has survived not only five centuries, but also the leap into electronic typesetting, remaining essentially unchanged. It was popularised in the 1960s with the release of printed sheets containing Lorem IpsumIpsum passages.</p>
    </div>
  </section>

  <div class="closing">
    <p>Yours Sincerely</p>
    <span class="signature-mark" role="img" aria-label="Handwritten signature of Daniel Whitcombe"></span>
    <p class="signer-name">Daniel Whitcombe</p>
    <p class="signer-title">Managing Director</p>
  </div>

  <footer class="footer-contact">
    <p class="footer-line-top"><span class="accent">P:</span> (404) 731-2864<span class="sep">|</span>www.<span class="accent">LarkmoorFirm</span>.legal</p>
    <p>418 Linden Ave., NW Atlanta, Georgia 30308<span class="sep-green">|</span>5120 Elm Ridge Rd. Douglasville, Georgia 30135</p>
  </footer>
</main>
</body>
</html>
```